this is a new company aimed at the automotive glass industry
what we do is repair cracked windscreens its based in western austraila
I like the old dragracing signwritting logos
I want it to stand out thats why ive gone with the name and title
I dont have a logo but if you can think of one that would be great
but not essential
on the back of the business card i would like Quicker Cheaper Better

Reason: More time needed to decide some great designs Have come through on the eleventh

Target Market(s)

automotive (car yards ,car auctions , trucking companys ect )

Industry/Entity Type

Automotive

Contact Information for Business Card

Pane Stoppers ,
Glass Crack repair specialists ,
Dorian Pelletier ,0437 612 084 ,dpelletier@panestopperswa.com.au

```html
<!DOCTYPE html>
<html lang="en">
<head>
<meta charset="utf-8">
<title>Pane Stoppers – Business Card</title>
<link rel="stylesheet" href="https://fonts.googleapis.com/css2?family=Bebas+Neue&family=Roboto:wght@400&display=swap">
<style>
  :root {
    --bg: #ebebeb;
    --front-blue: #18a2e2;
    --front-blue-deep: #0b8dd3;
    --ink-dark: #0f1b28;
    --back-navy: #03142a;
    --back-text: #f2f4f7;
    --crack-tint: rgba(255, 255, 255, 0.16);
    --card-shadow: 0 10px 24px rgba(0, 0, 0, 0.22);
  }
  * { margin: 0; padding: 0; box-sizing: border-box; }
  html, body {
    width: 1200px;
    height: 900px;
    overflow: hidden;
    background: var(--bg);
  }
  .stage {
    width: 1200px;
    height: 900px;
    display: flex;
    align-items: center;
    justify-content: center;
    gap: 40px;
  }
  .card {
    position: relative;
    width: 520px;
    height: 312px;
    box-shadow: var(--card-shadow);
    overflow: hidden;
  }

  /* Front */
  .card--front {
    background: linear-gradient(160deg, var(--front-blue) 0%, var(--front-blue-deep) 100%);
  }
  .front__crack {
    position: absolute;
    left: 130px;
    top: 20px;
    width: 260px;
    height: 260px;
    border-radius: 50%;
    background: radial-gradient(circle, var(--crack-tint) 0%, rgba(255,255,255,0) 70%);
  }
  .brand {
    position: absolute;
    left: 0;
    right: 0;
    top: 52px;
    text-align: center;
    color: var(--ink-dark);
    font-family: "Bebas Neue", sans-serif;
  }
  .brand__name {
    font-size: 92px;
    line-height: 0.86;
    letter-spacing: 1px;
  }
  .brand__tagline {
    margin-top: 6px;
    font-size: 17px;
    letter-spacing: 1.2px;
    color: var(--back-text);
  }

  /* Back */
  .card--back {
    background: var(--back-navy);
    color: var(--back-text);
  }
  .back__crack {
    position: absolute;
    left: 280px;
    top: 14px;
    width: 150px;
    height: 140px;
    border-radius: 50%;
    background: radial-gradient(circle, rgba(255,255,255,0.14) 0%, rgba(255,255,255,0) 70%);
  }
  .slogan {
    position: absolute;
    left: 28px;
    top: 34px;
    font-family: "Bebas Neue", sans-serif;
    font-size: 34px;
    line-height: 0.98;
    letter-spacing: 1.4px;
    list-style: none;
  }
  .contact {
    position: absolute;
    right: 30px;
    top: 154px;
    text-align: right;
  }
  .contact__name {
    font-family: "Roboto", sans-serif;
    font-size: 26px;
    line-height: 1.1;
  }
  .contact__phone {
    font-family: "Bebas Neue", sans-serif;
    font-size: 54px;
    line-height: 1;
    letter-spacing: 1.5px;
    margin-top: 4px;
  }
  .contact__email {
    font-family: "Roboto", sans-serif;
    font-size: 19px;
    margin-top: 4px;
  }
</style>
</head>
<body>
  <main class="stage">
    <section class="card card--front" aria-label="Business card front">
      <div class="front__crack" role="img" aria-label="Cracked windscreen glass graphic"></div>
      <div class="brand">
        <div class="brand__name">Pane<br>Stoppers</div>
        <div class="brand__tagline">Glass Crack Repair Specialists</div>
      </div>
    </section>

    <section class="card card--back" aria-label="Business card back">
      <div class="back__crack" role="img" aria-label="Cracked glass impact graphic"></div>
      <ul class="slogan">
        <li>Quicker</li>
        <li>Cheaper</li>
        <li>Better</li>
      </ul>
      <div class="contact">
        <p class="contact__name">Dorian Pelletier</p>
        <p class="contact__phone">0437 612 084</p>
        <p class="contact__email">dpelletier@panestopperswa.com.au</p>
      </div>
    </section>
  </main>
</body>
</html>
```